Jewelry Shop Needs a Cash Coupon Design

Mabel’s Nook is a Hong Kong based fine jewelry brand. We need a Cash Coupon for marketing promotion use.
Size: 1/6 A4 Size (want to print 6 pieces in one A4 paper)
Font Content:
1. Company Logo
2. HKD 500
3. 现金券 Cash Voucher
4. Jewelry Willow Hall
5. 香港九龍油麻地平安街18-22號福林大廈5樓
5/F , Fairgrove Tower, 18-22 Ping On Street, YMT, HK
T: +852 29480517 F: +852 29480519 M: info@mabels-nook.example
Back Content:
1. Terms and Conditions
Mabel’s Nook philosophy is a jewelry icon of young, creative, trendy, fashionable, stylish, energetic, and elegant. For Mabel’s Nook, jewelry is one collection of artworks, the most important items in personal life.
Marketing

```html
<!DOCTYPE html>
<html lang="en">
<head>
<meta charset="utf-8">
<title>Mabel’s Nook – HKD 500 Cash Voucher</title>
<link rel="stylesheet" href="https://fonts.googleapis.com/css2?family=Roboto+Condensed:wght@300;400;700&family=Noto+Sans+HK:wght@400;500&display=swap">
<style>
  :root {
    --backdrop: #b4b4b4;
    --paper: #ffffff;
    --ink: #000000;
    --reverse: #ffffff;
    --photo-light: #f2f3f5;
    --photo-mid: #d9dce0;
  }
  * { margin: 0; padding: 0; box-sizing: border-box; }
  html, body {
    width: 1200px; height: 1000px; overflow: hidden;
    background: var(--backdrop);
    font-family: "Roboto Condensed", "Arial Narrow", sans-serif;
    color: var(--ink);
  }
  .sheet { position: relative; width: 1200px; height: 1000px; }

  .voucher {
    position: absolute; top: 265px; width: 221px; height: 469px;
    background: var(--paper);
  }
  .voucher--a { left: 125px; }
  .voucher--b { left: 367px; }
  .voucher--c { left: 610px; }
  .voucher--back { left: 854px; }

  .brand {
    position: absolute; top: 21px; left: 0; width: 100%;
    display: flex; flex-direction: column; align-items: center;
  }
  .brand__dot { width: 38px; height: 38px; border-radius: 50%; background: var(--ink); }
  .brand__name {
    margin-top: 8px; font-size: 8.5px; font-weight: 700;
    letter-spacing: 0.6px; text-transform: uppercase; line-height: 1;
  }

  .product-photo {
    position: absolute; left: 28px; top: 87px; width: 165px; height: 167px;
    background: radial-gradient(ellipse at 50% 45%, var(--photo-light) 0%, var(--photo-mid) 100%);
  }

  .offer {
    position: absolute; left: 28px; top: 254px; width: 165px; height: 149px;
    background: var(--ink); color: var(--reverse);
    padding: 62px 0 0 19px;
  }
  .offer__amount, .offer__title {
    font-size: 24px; font-weight: 700; line-height: 24px; letter-spacing: -0.3px;
    display: block;
  }
  .offer__tagline { display: block; font-size: 12px; font-weight: 300; line-height: 14px; margin-top: 2px; }

  .contact {
    position: absolute; left: 0; bottom: 0; width: 100%; height: 62px;
    background: var(--ink); color: var(--reverse); text-align: center;
    padding-top: 12px;
  }
  .contact__zh { font-family: "Noto Sans HK", sans-serif; font-size: 9.5px; line-height: 13px; }
  .contact__en { font-size: 7.2px; font-weight: 700; line-height: 12px; white-space: nowrap; }

  .voucher--back .terms-panel {
    position: absolute; left: 0; top: 0; width: 100%; height: 440px;
    background: var(--ink); color: var(--reverse);
    padding: 24px 14px 0 12px;
  }
  .terms-zh { font-family: "Noto Sans HK", sans-serif; font-size: 4.6px; line-height: 7.6px; }
  .terms-zh h3 { font-size: 4.8px; font-weight: 500; margin-bottom: 3px; }
  .terms-zh ol { padding-left: 12px; }
  .terms-en { margin-top: 48px; font-size: 6.4px; line-height: 10.6px; }
  .terms-en h3 { font-size: 6.6px; font-weight: 700; padding-left: 29px; margin-bottom: 1px; }
  .terms-en ol { padding-left: 29px; }
  .terms-en li { text-align: justify; }
</style>
</head>
<body>
<main class="sheet">

  <article class="voucher voucher--a">
    <div class="brand"><span class="brand__dot"></span><span class="brand__name">Mabel’s Nook</span></div>
    <div class="product-photo" role="img" aria-label="Photo of a white-gold emerald-cut diamond ring with pavé band"></div>
    <div class="offer"><span class="offer__amount">HKD 500</span><span class="offer__title">Cash Voucher</span><span class="offer__tagline">Jewelry Willow Hall</span></div>
    <footer class="contact">
      <p class="contact__zh">香港九龍油麻地平安街18-22號福林大廈5樓</p>
      <p class="contact__en">5/F , Fairgrove Tower, 18-22 Ping On Street, YMT, HK</p>
      <p class="contact__en">T: +852 29480517 F: +852 29480519 M: info@mabels-nook.example</p>
    </footer>
  </article>

  <article class="voucher voucher--b">
    <div class="brand"><span class="brand__dot"></span><span class="brand__name">Mabel’s Nook</span></div>
    <div class="product-photo" role="img" aria-label="Photo of a diamond solitaire engagement ring with matching band"></div>
    <div class="offer"><span class="offer__amount">HKD 500</span><span class="offer__title">Cash Voucher</span><span class="offer__tagline">Jewelry Willow Hall</span></div>
    <footer class="contact">
      <p class="contact__zh">香港九龍油麻地平安街18-22號福林大廈5樓</p>
      <p class="contact__en">5/F , Fairgrove Tower, 18-22 Ping On Street, YMT, HK</p>
      <p class="contact__en">T: +852 29480517 F: +852 29480519 M: info@mabels-nook.example</p>
    </footer>
  </article>

  <article class="voucher voucher--c">
    <div class="brand"><span class="brand__dot"></span><span class="brand__name">Mabel’s Nook</span></div>
    <div class="product-photo" role="img" aria-label="Photo of a white-gold diamond ring with halo setting"></div>
    <div class="offer"><span class="offer__amount">HKD 500</span><span class="offer__title">Cash Voucher</span><span class="offer__tagline">Jewelry Willow Hall</span></div>
    <footer class="contact">
      <p class="contact__zh">香港九龍油麻地平安街18-22號福林大廈5樓</p>
      <p class="contact__en">5/F , Fairgrove Tower, 18-22 Ping On Street, YMT, HK</p>
      <p class="contact__en">T: +852 29480517 F: +852 29480519 M: info@mabels-nook.example</p>
    </footer>
  </article>

  <article class="voucher voucher--back">
    <div class="terms-panel">
      <section class="terms-zh" lang="zh-Hant">
        <h3>現金券條款及細則</h3>
        <ol>
          <li>此現金券乃本公司(Mabel’s Nook)的購物現金回贈券，顧客於本公司購物滿港幣$5000或以上(以發票上所示的購物金額為準)，並成功申請成為本公司VIP會員，即可獲贈HK$500現金回贈。</li>
          <li>每位合資格客戶每次購物滿港幣$5000或以上可使用一張現金回贈券，滿港幣$10000或以上可使用兩張，如此類推，不設上限。</li>
          <li>現金券的使用細則須受本公司相關條款限制，如有遺失或損毀，本公司恕不補發。</li>
          <li>本公司保留修改、暫停或取消以上優惠及條款之權利，毋須另行通知。如有任何爭議，本公司保留最終決定權。</li>
          <li>如條款中英文版本有任何歧異，一概以中文版為準。</li>
        </ol>
      </section>
      <section class="terms-en">
        <h3>The Cash Coupon Terms and Conditions</h3>
        <ol>
          <li>The cash coupon is the cash reward of shopping in Mabel’s Nook. Those consumers having purchased $5000 or above in our company every time (be subject to the shopping amount shown on the invoice, calculated on the same invoice as required), and successfully applied for the VIP members of our company, will be presented with HK$500 cash reward.</li>
          <li>Each qualified client can use one cash coupon if he purchases for HK$5000 or above every time; for HK$10000 or above can use two cash coupons and so on, no cap, purchase more and more in return.</li>
          <li>The using details of cash coupon must be subjected to the company’s related terms restrictions. Mabel’s Nook will not reissue or exchange cash coupons in case of any loss or defacement, or undertake any responsibility.</li>
          <li>This company reserves the right to modify, suspend or cancel the above privileges, terms and conditions, without prior notice. In case of disputes, this company reserves the right to make final decision.</li>
          <li>In case of any difference between the Chinese and English versions in the terms and conditions, the Chinese version shall prevail.</li>
        </ol>
      </section>
    </div>
  </article>

</main>
</body>
</html>
```